Wine labels Velmora Wine Council - Nueva etiqueta El Consejo Regulador de vinos de Albarrán

Velmora Wines Council, based in southern Spain, are looking to create a new suite of wine labels which retain the elegance of the Sherry Wines industry while reinvigorating their image to the modern era and a new generation of Sherry Wine lovers. These labels will be used across the Velmora Wines Council's range of wines for the promotion of the Sherry Wines industry.

Your design must present at least two styles of Sherry Wines which demonstrate an elegant, modern interpretation and understanding of the unique mood and personality for these wines and the essence of southern Spain.

10 labels will be created based on the winning design, one for each of the unique varieties of Sherry Wines within the collection. This collection comprises of several different wine varieties including: Fino, Manzanilla, Amontillado, Oloroso, Palo Cortado, Medium, Cream, Pale Cream, Pedro Ximenez and Moscatel.

We recommend you visit our website www.velmora-vinos.example/wines as the source to understanding the origins and unique personality of these diverse wines.

El Consejo Regulador de los Vinos de Albarrán y Tordesal quiere renovar las etiquetas de los vinos utilizados para sus actividades de promoción genérica. Esta colección de vinos comprende las tipologías más importantes de la región que incluye: fino, manzanilla, amontillado, oloroso, palo cortado, pale cream, medium, cream, pedro ximénez y moscatel. Por lo tanto se precisan 10 etiquetas, una para cada uno de los vinos mencionados.
Updates

Project Deadline Extended
Reason: Due to some confusion with the deadline we wish to officially extend the deadline to allow designers one last week to submit their entries.

Target Market(s)

Industry, journalists, media, sommeliers, chefs, wine writers

Industry/Entity Type

Council

Requirements
Must have
• Front and Back label plus capsule:
• Front label can have either of the two official logos of the Velmora Wine council titled Vinos de Albarrán Digital or not, this is optional. Must include: Vino selecionado por el Consejo Regulador de la Denominacion de Origen, Name of the variety of wine eg FINO, percentage of alcohol eg 15% and quantity 75 cl.
• The back of the label must include the council logo titled Sellora and 4 additional logos positioned smaller. The Europa logo must appear larger than the 3 other logos. Space for descriptive text about the wine is also required.
• The dimensions of the bottle can be found at this link http://www.vidrialto.example/es/catalogo/vinos-y-espumosos/bordelesas/bd-orla
• Altura:305 mm
• Diámetro base:76,20 mm
• Diámetro hombro:82 mm
• Tipo boca:Cetie
• Peso:750 gr
• Capacidad:75 cl
• Etiqueta delantera y trasera y capsula
• La etiqueta delantera puede incluir el logo oficial del Consejo Regulador o el logo digital, o ninguno, esto es opcional. Debe incluir el siguiete texto: Vino selecionado por el Consejo Regulador de la Denominacion de Origen, el nombre de la variedad del vino, por ejemplo Fino, el porcentaje de alcohol, por ejemplo 15%, y la capacidad 75cl.
• La etiqueta trasera debe incluir el logo oficial Sellora del Consejo, y cuatro logos adicionales con una dimension menor. El Logo de ¨Europa invierte en las zonas rurales¨ debe ser de mayor tamaño que los otros. Se precisa espacio para el texto descriptivo de los vinos.
• Las dimensiones de la botella se puede encontrar en este enlace
• http://www.vidrialto.example/es/catalogo/vinos-y-espumosos/bordelesas/bd-orla
• Altura:305 mm
• Diámetro base:76,20 mm
• Diámetro hombro:82 mm
• Tipo boca:Cetie
• Peso:750 gr
• Capacidad:75 cl
Nice to have
• See our website velmora-vinos.example to understand the origin of the wines. Ver nuestra página web velmora-vinos.example para mejor entender los vinos.
Should not have
• Images of catavinos or stereotypical images from Spain such as flamenco dancers or guitars.

```html
<!DOCTYPE html>
<html lang="es">
<head>
<meta charset="utf-8">
<title>Propuesta +b. — Etiquetas Velmora Wine Council</title>
<link rel="stylesheet" href="https://fonts.googleapis.com/css2?family=Bodoni+Moda:opsz,wght@6..96,400;6..96,500&display=swap">
<style>
  :root {
    --paper: #ffffff;
    --ink: #111111;
    --divider: #000000;
    --stage-light: #f5f5f5;
    --stage-dark: #e4e4e4;
    --glass: #1c0d0f;
    --glass-edge: #2b1418;
    --chalk-glow: rgba(255, 255, 255, 0.16);
    --chalk-fade: rgba(255, 255, 255, 0.05);
    --label: #f7f7f5;
    --label-ink: #2a2a2a;
    --cap-silver: #8d8a86;
    --cap-gold: #a39233;
    --cap-brown: #5a3218;
    --cap-umber: #4a2213;
    --cap-wine: #3b1510;
    --cap-black: #1e1a16;
  }
  * { box-sizing: border-box; margin: 0; padding: 0; }
  html, body { width: 1200px; height: 900px; overflow: hidden; background: var(--paper); }
  .board { position: relative; width: 1200px; height: 900px; background: var(--paper); color: var(--ink); font-family: "Bodoni Moda", serif; }

  .brief-panel { position: absolute; left: 0; top: 0; width: 408px; height: 900px; }
  .brief-title { position: absolute; left: 51px; top: 54px; font-weight: 400; font-size: 50px; line-height: 1.1; letter-spacing: 1px; }
  .brief-copy { position: absolute; left: 42px; top: 224px; width: 340px; font-size: 14px; line-height: 18px; font-weight: 400; }
  .brief-copy ul { list-style: none; }
  .brief-copy li { position: relative; padding-left: 27px; hyphens: auto; }
  .brief-copy li::before { content: "•"; position: absolute; left: 2px; top: 0; }
  .brief-copy h2 { font-size: 14px; font-weight: 400; margin: 14px 0 14px; }
  .brief-copy h2:first-of-type { margin-top: 16px; }

  .divider { position: absolute; left: 408px; top: 0; width: 9px; height: 900px; background: var(--divider); }

  .stage { position: absolute; left: 417px; top: 0; width: 783px; height: 900px; background: linear-gradient(135deg, var(--stage-light), var(--stage-dark)); }

  .bottle { position: absolute; width: 90px; }
  .bottle-shape { position: absolute; inset: 0; }
  .bottle-neck { position: absolute; left: 29px; top: 0; width: 32px; height: 130px; background: var(--glass); border-radius: 3px 3px 0 0; }
  .bottle-cap { position: absolute; left: 0; top: 0; width: 100%; height: 68px; border-radius: 3px 3px 0 0; }
  .bottle-body { position: absolute; left: 0; top: 112px; width: 90px; bottom: 0; background: linear-gradient(90deg, var(--glass-edge), var(--glass) 30%, var(--glass) 75%, var(--glass-edge)); border-radius: 36px 36px 4px 4px; }
  .top-row { top: 58px; height: 364px; }
  .bottom-row { top: 468px; height: 362px; }

  .chalk-symbol { position: absolute; left: 6px; top: 158px; width: 78px; height: 74px; border-radius: 4px; background: radial-gradient(ellipse at center, var(--chalk-glow), var(--chalk-fade) 70%, transparent); }

  .wine-label { position: absolute; left: 0; top: 236px; width: 90px; height: 52px; background: var(--label); color: var(--label-ink); display: flex; flex-direction: column; align-items: center; overflow: hidden; }
  .wine-name { height: 17px; margin-top: 7px; width: 100%; padding: 0 3px; display: flex; align-items: center; justify-content: center; white-space: nowrap; font-size: 13px; letter-spacing: 0.6px; }
  .wine-name--mid { font-size: 10.5px; letter-spacing: 0.3px; }
  .wine-name--long { font-size: 9px; letter-spacing: 0.1px; }
  .wine-note { margin-top: 4px; width: 72px; text-align: center; font-size: 3px; line-height: 4px; }
  .wine-volume { align-self: flex-end; margin: 3px 8px 0 0; font-size: 3px; }

  .cap-silver { background: var(--cap-silver); }
  .cap-gold { background: var(--cap-gold); }
  .cap-brown { background: var(--cap-brown); }
  .cap-umber { background: var(--cap-umber); }
  .cap-wine { background: var(--cap-wine); }
  .cap-black { background: var(--cap-black); }
</style>
</head>
<body>
<main class="board">
  <section class="brief-panel">
    <h1 class="brief-title">PROPUESTA<br>+b.</h1>
    <div class="brief-copy">
      <ul>
        <li>Este diseño está basado en las anotaciones que se hacían con tiza en las botas de la bodega para clasificar los tipos de vinos. Dichos dibujos están cargados de gran fuerza expresiva y de abstracción. Siendo un elemento de alto contenido simbólico y de tradición, son increíblemente modernos y atemporales.</li>
        <li>Tamaño: La serigrafía mide 7,5 cm. de alto aproximadamente y la etiqueta adhesiva 10x4,5 cm (anchura-altura).</li>
      </ul>
      <h2>TÉCNICA:</h2>
      <ul>
        <li>Símbolo: Serigrafía directa sobre el vidrio de la botella.</li>
        <li>Nombre del vino y datos informativos: impresión offset/digital en negro.</li>
      </ul>
      <h2>CÁPSULA:</h2>
      <ul>
        <li>Lisa del pantone correspondiente a cada vino.</li>
        <li>Símbolo correspondiente a cada tipo de vino estampado en seco la parte superior.</li>
      </ul>
    </div>
  </section>

  <div class="divider"></div>

  <section class="stage">
    <div class="bottle top-row" style="left:90px">
      <div class="bottle-shape"><div class="bottle-neck"><div class="bottle-cap cap-silver"></div></div><div class="bottle-body"></div></div>
      <div class="chalk-symbol" role="img" aria-label="Símbolo de tiza «PC» serigrafiado en blanco sobre el vidrio"></div>
      <div class="wine-label"><p class="wine-name wine-name--mid">PALE CREAM</p><p class="wine-note">Vino seleccionado por el Consejo Regulador de la Denominación de Origen</p><p class="wine-volume">75 cl</p></div>
    </div>
    <div class="bottle top-row" style="left:220px">
      <div class="bottle-shape"><div class="bottle-neck"><div class="bottle-cap cap-gold"></div></div><div class="bottle-body"></div></div>
      <div class="chalk-symbol" role="img" aria-label="Símbolo de tiza de trazos en ángulo serigrafiado en blanco"></div>
      <div class="wine-label"><p class="wine-name wine-name--mid">MANZANILLA</p><p class="wine-note">Vino seleccionado por el Consejo Regulador de la Denominación de Origen</p><p class="wine-volume">75 cl</p></div>
    </div>
    <div class="bottle top-row" style="left:352px">
      <div class="bottle-shape"><div class="bottle-neck"><div class="bottle-cap cap-gold"></div></div><div class="bottle-body"></div></div>
      <div class="chalk-symbol" role="img" aria-label="Símbolo de tiza de palma serigrafiado en blanco"></div>
      <div class="wine-label"><p class="wine-name">FINO</p><p class="wine-note">Vino seleccionado por el Consejo Regulador de la Denominación de Origen</p><p class="wine-volume">75 cl</p></div>
    </div>
    <div class="bottle top-row" style="left:484px">
      <div class="bottle-shape"><div class="bottle-neck"><div class="bottle-cap cap-brown"></div></div><div class="bottle-body"></div></div>
      <div class="chalk-symbol" role="img" aria-label="Símbolo de tiza de círculo con trazos serigrafiado en blanco"></div>
      <div class="wine-label"><p class="wine-name wine-name--mid">AMONTILLADO</p><p class="wine-note">Vino seleccionado por el Consejo Regulador de la Denominación de Origen</p><p class="wine-volume">75 cl</p></div>
    </div>
    <div class="bottle top-row" style="left:616px">
      <div class="bottle-shape"><div class="bottle-neck"><div class="bottle-cap cap-brown"></div></div><div class="bottle-body"></div></div>
      <div class="chalk-symbol" role="img" aria-label="Símbolo de tiza en forma de D cruzada serigrafiado en blanco"></div>
      <div class="wine-label"><p class="wine-name">MEDIUM</p><p class="wine-note">Vino seleccionado por el Consejo Regulador de la Denominación de Origen</p><p class="wine-volume">75 cl</p></div>
    </div>

    <div class="bottle bottom-row" style="left:90px">
      <div class="bottle-shape"><div class="bottle-neck"><div class="bottle-cap cap-umber"></div></div><div class="bottle-body"></div></div>
      <div class="chalk-symbol" role="img" aria-label="Símbolo de tiza de círculo tachado serigrafiado en blanco"></div>
      <div class="wine-label"><p class="wine-name">OLOROSO</p><p class="wine-note">Vino seleccionado por el Consejo Regulador de la Denominación de Origen</p><p class="wine-volume">75 cl</p></div>
    </div>
    <div class="bottle bottom-row" style="left:220px">
      <div class="bottle-shape"><div class="bottle-neck"><div class="bottle-cap cap-umber"></div></div><div class="bottle-body"></div></div>
      <div class="chalk-symbol" role="img" aria-label="Símbolo de tiza de raya cortada serigrafiado en blanco"></div>
      <div class="wine-label"><p class="wine-name wine-name--long">PALO CORTADO</p><p class="wine-note">Vino seleccionado por el Consejo Regulador de la Denominación de Origen</p><p class="wine-volume">75 cl</p></div>
    </div>
    <div class="bottle bottom-row" style="left:352px">
      <div class="bottle-shape"><div class="bottle-neck"><div class="bottle-cap cap-wine"></div></div><div class="bottle-body"></div></div>
      <div class="chalk-symbol" role="img" aria-label="Símbolo de tiza en forma de D con círculo serigrafiado en blanco"></div>
      <div class="wine-label"><p class="wine-name">CREAM</p><p class="wine-note">Vino seleccionado por el Consejo Regulador de la Denominación de Origen</p><p class="wine-volume">75 cl</p></div>
    </div>
    <div class="bottle bottom-row" style="left:484px">
      <div class="bottle-shape"><div class="bottle-neck"><div class="bottle-cap cap-umber"></div></div><div class="bottle-body"></div></div>
      <div class="chalk-symbol" role="img" aria-label="Símbolo de tiza «ME» serigrafiado en blanco"></div>
      <div class="wine-label"><p class="wine-name wine-name--mid">MOSCATEL</p><p class="wine-note">Vino seleccionado por el Consejo Regulador de la Denominación de Origen</p><p class="wine-volume">75 cl</p></div>
    </div>
    <div class="bottle bottom-row" style="left:616px">
      <div class="bottle-shape"><div class="bottle-neck"><div class="bottle-cap cap-black"></div></div><div class="bottle-body"></div></div>
      <div class="chalk-symbol" role="img" aria-label="Símbolo de tiza «PX» serigrafiado en blanco"></div>
      <div class="wine-label"><p class="wine-name wine-name--long">PEDRO XIMÉNEZ</p><p class="wine-note">Vino seleccionado por el Consejo Regulador de la Denominación de Origen</p><p class="wine-volume">75 cl</p></div>
    </div>
  </section>
</main>
</body>
</html>
```